Email Notification & Marketing Templates

I want to start with something like a newsletter or informational email, but i need Top Tips to Detect Phishing Scams. Something that i can send to users so they can follow it when receiving or exchanging emails. I will also need promotional items for my company that i can send to customers as well. It can be based on on our website PLVORIX.COM

Will also need:
newsletters
announcements
marketing emails
alerts
security notifications

Examples:Items such as Security Awareness Poster Series
Phishing Awareness
Password Security
Email Attachments
QR Code scams
Public WiFi safety

```html
<!DOCTYPE html>
<html lang="en">
<head>
<meta charset="utf-8">
<title>Plvorix – Stay Safe on Public WiFi</title>
<link rel="stylesheet" href="https://fonts.googleapis.com/css2?family=Cabin:wght@400;500;600;700&display=swap">
<style>
  :root {
    --page-bg: #f1f1f1;
    --card-bg: #ffffff;
    --green-dark: #1f5e1c;
    --green: #2f7d24;
    --green-bright: #5fb83a;
    --ink: #222222;
    --ink-soft: #3a3a3a;
    --hairline: #e3e6e3;
  }
  * { box-sizing: border-box; margin: 0; padding: 0; }
  html, body { width: 800px; height: 1200px; overflow: hidden; }
  body {
    background: var(--page-bg);
    font-family: "Cabin", Arial, sans-serif;
    color: var(--ink);
    position: relative;
  }
  .email {
    position: absolute; left: 84px; top: 52px;
    width: 632px; height: 1148px;
    background: var(--card-bg);
    box-shadow: 0 0 6px rgba(0,0,0,0.06);
  }
  .brand {
    position: absolute; left: 31px; top: 34px;
    display: flex; align-items: center; gap: 10px;
  }
  .brand-square { width: 22px; height: 22px; background: var(--green); }
  .brand-name {
    font-size: 40px; font-weight: 700; color: var(--green);
    letter-spacing: 1px; line-height: 1;
  }
  .headline {
    position: absolute; left: 29px; top: 132px;
    font-size: 38px; font-weight: 600; color: var(--green-dark);
    letter-spacing: -0.3px;
  }
  .intro {
    position: absolute; left: 30px; top: 183px; width: 560px;
    font-size: 16.5px; line-height: 25px; color: var(--ink);
  }
  .hero {
    position: absolute; left: 0; top: 244px; width: 632px; height: 296px;
    background: radial-gradient(ellipse at 62% 50%, #8fcf86 0%, #6a8a58 30%, #7a5c3e 65%, #4a3828 100%);
  }
  .tips { position: absolute; left: 30px; top: 564px; width: 580px; list-style: none; }
  .tip { display: flex; gap: 12px; margin-bottom: 14px; }
  .tip svg { flex: none; width: 26px; height: 26px; margin-top: 1px; }
  .tip-title { font-size: 18px; font-weight: 600; color: var(--green-dark); line-height: 24px; }
  .tip-text { font-size: 15.5px; line-height: 20px; color: var(--ink); }
  .band {
    position: absolute; left: 0; top: 793px; width: 632px; height: 46px;
    background: linear-gradient(90deg, var(--green-dark), var(--green) 60%, #4a9a2c);
    color: #fff; font-size: 25px; font-weight: 500;
    display: flex; align-items: center; justify-content: center;
  }
  .solutions-title {
    position: absolute; left: 30px; top: 852px;
    font-size: 21px; font-weight: 600; color: var(--green-dark);
  }
  .solutions-text {
    position: absolute; left: 30px; top: 885px; width: 580px;
    font-size: 15.5px; line-height: 23px; color: var(--ink);
  }
  .services {
    position: absolute; left: 30px; top: 950px; width: 580px;
    display: grid; grid-template-columns: 298px 282px; row-gap: 14px;
  }
  .service { display: flex; gap: 10px; }
  .service:nth-child(even) { border-left: 1px solid var(--hairline); padding-left: 14px; }
  .service svg { flex: none; width: 30px; height: 34px; }
  .service-title { font-size: 17.5px; font-weight: 600; color: var(--ink); line-height: 22px; }
  .service-text { font-size: 14.5px; line-height: 19px; color: var(--ink-soft); }
  .cta {
    position: absolute; left: 168px; top: 1096px; width: 286px; height: 41px;
    background: linear-gradient(180deg, #3e9a2c, var(--green));
    border-radius: 3px; color: #fff; font-size: 20px; font-weight: 500;
    display: flex; align-items: center; justify-content: center;
    box-shadow: 0 2px 4px rgba(0,0,0,0.2);
  }
</style>
</head>
<body>
<main class="email">
  <header class="brand">
    <span class="brand-square"></span>
    <span class="brand-name">PLVORIX</span>
  </header>
  <h1 class="headline">Stay Safe on Public WiFi</h1>
  <p class="intro">Using public WiFi can put your sensitive information at risk. Follow these tips to stay secure.</p>

  <div class="hero" role="img" aria-label="Photo of a man working on a laptop in a busy café, surrounded by a glowing green security shield"></div>

  <ul class="tips">
    <li class="tip">
      <svg viewBox="0 0 26 26"><circle cx="13" cy="13" r="13" fill="#4cae3a"/><path d="M7 13.5l4 4 8-8" stroke="#fff" stroke-width="2.8" fill="none" stroke-linecap="round" stroke-linejoin="round"/></svg>
      <div><h2 class="tip-title">Avoid Sensitive Logins.</h2><p class="tip-text">Refrain from accessing sensitive accounts like banking or email over public WiFi.</p></div>
    </li>
    <li class="tip">
      <svg viewBox="0 0 26 26"><circle cx="13" cy="13" r="13" fill="#4cae3a"/><path d="M7 13.5l4 4 8-8" stroke="#fff" stroke-width="2.8" fill="none" stroke-linecap="round" stroke-linejoin="round"/></svg>
      <div><h2 class="tip-title">Use a VPN</h2><p class="tip-text">Utilize a Virtual Private Network (VPN) to encrypt your internet connection.</p></div>
    </li>
    <li class="tip">
      <svg viewBox="0 0 26 26"><circle cx="13" cy="13" r="13" fill="#4cae3a"/><path d="M7 13.5l4 4 8-8" stroke="#fff" stroke-width="2.8" fill="none" stroke-linecap="round" stroke-linejoin="round"/></svg>
      <div><h2 class="tip-title">Verify Networks</h2><p class="tip-text">Confirm the legitimacy of the WiFi network before connecting to avoid fake hotspots.</p></div>
    </li>
  </ul>

  <div class="band">Protect Your Business</div>
  <h2 class="solutions-title">Comprehensive Cybersecurity Solutions</h2>
  <p class="solutions-text">Plvorix Networks offers robust cybersecurity services to protect your business from online threats. Contact us to learn how we can</p>

  <section class="services">
    <div class="service">
      <svg viewBox="0 0 30 34"><path d="M15 1L28 6v10c0 9-6 14-13 17C8 30 2 25 2 16V6z" fill="#2f7d24"/><path d="M15 5l9 3.5v7.5c0 6-4 10-9 12.5C10 26 6 22 6 16V8.5z" fill="#fff"/><path d="M10 17l3.5 3.5 6.5-7" stroke="#2f7d24" stroke-width="2.4" fill="none"/></svg>
      <div><h3 class="service-title">Network Security</h3><p class="service-text">Firewall, intrusion detection/ prevention</p></div>
    </div>
    <div class="service">
      <svg viewBox="0 0 30 34"><path d="M15 1L28 6v10c0 9-6 14-13 17C8 30 2 25 2 16V6z" fill="#2f7d24"/><rect x="8" y="11" width="14" height="10" rx="1.5" fill="#fff"/><rect x="11" y="15" width="8" height="2" fill="#2f7d24"/></svg>
      <div><h3 class="service-title">Endpoint Protection</h3><p class="service-text">Antivirus and malware defense</p></div>
    </div>
    <div class="service">
      <svg viewBox="0 0 30 34"><path d="M15 1L28 6v10c0 9-6 14-13 17C8 30 2 25 2 16V6z" fill="#2f7d24"/><rect x="9.5" y="15" width="11" height="9" rx="1.5" fill="#fff"/><path d="M11.5 15v-3a3.5 3.5 0 017 0v3" stroke="#fff" stroke-width="2" fill="none"/><circle cx="15" cy="19.5" r="1.5" fill="#2f7d24"/></svg>
      <div><h3 class="service-title">Data Encryption</h3><p class="service-text">Safeguard sensitive information</p></div>
    </div>
    <div class="service">
      <svg viewBox="0 0 30 34"><path d="M15 1L28 6v10c0 9-6 14-13 17C8 30 2 25 2 16V6z" fill="#2f7d24"/><circle cx="15" cy="16" r="7" fill="#fff"/><path d="M15 12v4l3 2" stroke="#2f7d24" stroke-width="2" fill="none"/></svg>
      <div><h3 class="service-title">24/7 Monitoring</h3><p class="service-text">Proactive threat detection and response.</p></div>
    </div>
  </section>

  <a class="cta">Get a Free Consultation</a>
</main>
</body>
</html>
```